Bifold for voip company

Bifold for cloud voip company

Target Market(s)

Business owners

Industry/Entity Type

Software Developer

Colors

Designer to choose colors to be used in the design.

Requirements
Must have
• Modern clean design,
• will provide content to design winner

```html
<!DOCTYPE html>
<html lang="en">
<head>
<meta charset="utf-8">
<title>Nimbra Bifold Brochure</title>
<link href="https://fonts.googleapis.com/css2?family=Open+Sans:wght@300;400;600&family=Audiowide&display=swap" rel="stylesheet">
<style>
  :root {
    --blue: #1b8fc4;
    --blue-light: #2aa7d6;
    --blue-deep: #167bab;
    --purple: #8b58c8;
    --purple-deep: #6b3fa8;
    --paper: #f1f2f4;
    --panel-shade: #e6e8eb;
    --ink: #3c3c3c;
    --ink-soft: #6a6a6a;
    --stage: #e9e9e9;
  }
  * { box-sizing: border-box; margin: 0; padding: 0; }
  html, body { width: 1200px; height: 1200px; overflow: hidden; }
  body {
    position: relative;
    background: var(--stage);
    font-family: "Open Sans", Arial, sans-serif;
    color: var(--ink);
  }
  .side-label {
    position: absolute;
    left: 70px;
    font-family: "Audiowide", "Open Sans", sans-serif;
    font-size: 22px;
    color: #111;
  }
  .side-label--outside { top: 18px; }
  .side-label--inside { top: 578px; }

  .spread {
    position: absolute;
    left: 70px;
    width: 1060px;
    background: var(--paper);
    box-shadow: 0 6px 18px rgba(0,0,0,.12);
    overflow: hidden;
  }
  .spread--outside { top: 55px; height: 500px; }
  .spread--inside { top: 615px; height: 540px; }
  .spread__art { position: absolute; inset: 0; }
  .fold { position: absolute; top: 0; bottom: 0; left: 530px; width: 1px; background: rgba(0,0,0,.08); }

  /* Outside: back panel */
  .about__title {
    position: absolute; left: 42px; top: 205px;
    font-weight: 300; font-size: 50px; color: var(--blue); letter-spacing: 1px;
  }
  .about__body { position: absolute; left: 44px; top: 278px; width: 440px; }
  .about__body p { font-size: 9px; line-height: 1.5; color: var(--ink-soft); margin-bottom: 8px; }
  .contact { position: absolute; left: 30px; top: 425px; list-style: none; }
  .contact li {
    display: flex; align-items: center; gap: 8px;
    color: #fff; font-size: 11px; margin-bottom: 5px;
  }
  .contact svg { width: 16px; height: 16px; flex: none; }

  /* Outside: cover panel */
  .tagline { position: absolute; left: 610px; top: 200px; }
  .tagline__small {
    display: inline-block; margin-left: 60px;
    background: var(--blue); color: #fff; font-size: 11px; font-weight: 600;
    padding: 2px 10px;
  }
  .tagline__main {
    display: block; width: max-content;
    background: var(--blue-light); color: #fff; font-size: 22px; font-weight: 600;
    padding: 1px 14px; letter-spacing: 1px;
  }
  .brand {
    position: absolute; display: flex; align-items: center; gap: 14px;
    font-weight: 600; color: #555; letter-spacing: 4px;
  }
  .brand__mark { background: var(--purple); flex: none; }
  .brand--cover { left: 620px; top: 290px; font-size: 70px; }
  .brand--cover .brand__mark { width: 34px; height: 34px; }
  .brand--inside { left: 60px; top: 30px; font-size: 44px; }
  .brand--inside .brand__mark { width: 22px; height: 22px; }

  /* Inside */
  .pill {
    display: inline-block; border-radius: 14px; color: #fff;
    font-size: 13px; padding: 3px 16px; white-space: nowrap;
  }
  .pill--blue { background: var(--blue-light); }
  .pill--purple { background: var(--purple); }
  .topic { position: absolute; width: 145px; }
  .topic p { font-size: 8px; line-height: 1.5; color: var(--ink-soft); margin-top: 6px; padding-left: 6px; }

  .gallery__item { position: absolute; width: 120px; height: 120px; padding: 9px; }
  .gallery__item--purple { background: var(--purple); }
  .gallery__item--blue { background: var(--blue-light); }
  .gallery__photo { width: 100%; height: 100%; }
  .gallery__label { position: absolute; font-size: 11px; padding: 2px 12px; }

  .article { position: absolute; left: 562px; width: 470px; }
  .article h3 { font-weight: 400; font-size: 15px; margin-bottom: 4px; }
  .article--one h3 { color: var(--purple); }
  .article--two h3 { color: var(--blue-light); }
  .article p { font-size: 8px; line-height: 1.5; color: var(--ink-soft); }
</style>
</head>
<body>

<div class="side-label side-label--outside">Outside</div>
<section class="spread spread--outside">
  <svg class="spread__art" viewBox="0 0 1060 500" width="1060" height="500">
    <defs>
      <linearGradient id="lockPhoto" x1="0" y1="0" x2="1" y2="1">
        <stop offset="0" stop-color="#9fd3ec"/><stop offset="1" stop-color="#1f6f9c"/>
      </linearGradient>
      <linearGradient id="callPhoto" x1="0" y1="0" x2="1" y2="1">
        <stop offset="0" stop-color="#4b4b52"/><stop offset=".6" stop-color="#a0795f"/><stop offset="1" stop-color="#2d2d33"/>
      </linearGradient>
      <linearGradient id="globePhoto" x1="0" y1="0" x2="1" y2="1">
        <stop offset="0" stop-color="#2a3550"/><stop offset=".55" stop-color="#8fc3ea"/><stop offset="1" stop-color="#c99a7a"/>
      </linearGradient>
    </defs>
    <rect x="530" y="0" width="530" height="500" fill="#f4f5f6"/>
    <polygon points="0,0 160,0 0,120" fill="var(--panel-shade)"/>
    <polygon points="40,0 265,195 490,0 430,0 265,140 100,0" fill="var(--blue)"/>
    <g role="img" aria-label="Photo of a businessman's hand and a digital padlock, security theme">
      <polygon points="115,0 265,128 415,0" fill="url(#lockPhoto)"/>
    </g>
    <polygon points="0,395 530,435 530,500 0,500" fill="var(--blue-deep)"/>
    <polygon points="0,380 530,425 530,435 0,395" fill="var(--blue-light)"/>

    <polygon points="555,0 745,180 930,0 865,0 745,118 620,0" fill="var(--purple)"/>
    <g role="img" aria-label="Photo of a hand touching a phone call icon among contact icons">
      <polygon points="640,0 745,100 845,0" fill="url(#callPhoto)"/>
    </g>
    <polygon points="820,55 965,320 1060,200 1060,160 965,262 880,55" fill="var(--blue-light)"/>
    <g role="img" aria-label="Photo of a hand with a tablet and a glowing globe of network screens">
      <polygon points="885,55 1060,55 1060,150 965,250" fill="url(#globePhoto)"/>
    </g>
    <polygon points="530,410 1060,455 1060,500 530,500" fill="var(--blue-light)"/>
    <polygon points="530,400 1060,445 1060,455 530,410" fill="var(--blue)"/>
  </svg>
  <div class="fold"></div>

  <h2 class="about__title">ABOUT US</h2>
  <div class="about__body">
    <p>We build cloud phone systems for growing businesses. Our team sets up calls, voicemail and video in one simple place, so your staff can talk to customers from any desk, laptop or phone without extra hardware.</p>
    <p>Every plan includes clear pricing, secure lines and friendly support. Move numbers, add users and track call quality from one dashboard that grows with you.</p>
  </div>
  <ul class="contact">
    <li><svg viewBox="0 0 16 16"><circle cx="8" cy="8" r="7" fill="none" stroke="#fff" stroke-width="1.3"/><path d="M1 8h14M8 1c3 3 3 11 0 14M8 1c-3 3-3 11 0 14" fill="none" stroke="#fff" stroke-width="1"/></svg>www.nimbravoice.com</li>
    <li><svg viewBox="0 0 16 16"><path d="M4 2l3 3-2 2c1 2 2 3 4 4l2-2 3 3-2 2C7 14 2 9 2 4z" fill="#fff"/></svg>0800 - 555 010 020 030</li>
    <li><svg viewBox="0 0 16 16"><path d="M8 1a5 5 0 0 1 5 5c0 4-5 9-5 9S3 10 3 6a5 5 0 0 1 5-5z" fill="#fff"/><circle cx="8" cy="6" r="2" fill="var(--blue-deep)"/></svg>12 Harbour Line Avenue</li>
  </ul>

  <div class="tagline">
    <span class="tagline__small">Communications</span>
    <span class="tagline__main">Simplified</span>
  </div>
  <div class="brand brand--cover"><span class="brand__mark"></span>NIMBRA</div>
</section>

<div class="side-label side-label--inside">Inside</div>
<section class="spread spread--inside">
  <svg class="spread__art" viewBox="0 0 1060 540" width="1060" height="540">
    <rect x="530" y="0" width="530" height="540" fill="#f6f6f7"/>
    <g role="img" aria-label="Blue geometric triangle pattern">
      <polygon points="420,0 530,0 530,105" fill="var(--blue-light)"/>
      <polygon points="530,0 1060,0 1060,110 530,95" fill="var(--blue-light)"/>
    </g>
    <path d="M110 332 C 200 335, 300 380, 330 460" fill="none" stroke="var(--blue)" stroke-width="2"/>
  </svg>
  <div class="fold"></div>

  <div class="brand brand--inside"><span class="brand__mark"></span>NIMBRA</div>

  <div class="topic" style="left:40px;top:120px"><span class="pill pill--blue">Headings 1</span><p>Set up your office line in minutes and keep every call in the cloud.</p></div>
  <div class="topic" style="left:200px;top:120px"><span class="pill pill--purple">Headings 2</span><p>Route calls to the right person with smart menus and simple rules.</p></div>
  <div class="topic" style="left:360px;top:120px"><span class="pill pill--blue">Headings 3</span><p>Join voice, video and chat so your team stays close wherever they work.</p></div>

  <span class="pill pill--blue gallery__label" style="left:70px;top:318px">Label 1</span>
  <div class="gallery__item gallery__item--purple" style="left:40px;top:345px">
    <div class="gallery__photo" role="img" aria-label="Glowing blue digital brain illustration" style="background:radial-gradient(circle,#3a7de0,#0b1640)"></div>
  </div>
  <span class="pill pill--purple gallery__label" style="left:215px;top:318px">Label 2</span>
  <div class="gallery__item gallery__item--blue" style="left:190px;top:345px">
    <div class="gallery__photo" role="img" aria-label="Photo of a hand tapping network icons on a screen" style="background:linear-gradient(135deg,#d7dce2,#8a6a55)"></div>
  </div>
  <span class="pill pill--blue gallery__label" style="left:365px;top:318px">Label 3</span>
  <div class="gallery__item gallery__item--purple" style="left:340px;top:345px">
    <div class="gallery__photo" role="img" aria-label="Blue cloud network technology illustration" style="background:linear-gradient(135deg,#1d3f9a,#4fb0ef)"></div>
  </div>

  <div class="topic" style="left:565px;top:125px"><span class="pill pill--purple">Headings 1</span><p>Clear monthly plans with no hidden fees or long contracts.</p></div>
  <div class="topic" style="left:725px;top:125px"><span class="pill pill--blue">Headings 2</span><p>Keep your current numbers and move them over at no cost.</p></div>
  <div class="topic" style="left:885px;top:125px"><span class="pill pill--purple">Headings 3</span><p>Encrypted lines protect every call and message you send.</p></div>
  <div class="topic" style="left:565px;top:235px"><span class="pill pill--blue">Headings 4</span><p>Add new users from the dashboard in just a few clicks.</p></div>
  <div class="topic" style="left:725px;top:235px"><span class="pill pill--purple">Headings 5</span><p>Call reports show volume, wait times and missed calls at a glance.</p></div>
  <div class="topic" style="left:885px;top:235px"><span class="pill pill--blue">Headings 6</span><p>Real people answer support requests every day of the week.</p></div>

  <div class="article article--one" style="top:350px">
    <h3>Paragraph Header Number One</h3>
    <p>Our platform runs on secure data centres with backup power, so your lines stay live during outages. Calls forward to mobiles automatically and voicemail arrives in your inbox as audio.</p>
  </div>
  <div class="article article--two" style="top:430px">
    <h3>Paragraph Header Number Two</h3>
    <p>Switching is easy. We plan the move with you, test every line before launch and train your staff, so the first day on the new system feels like any other working day.</p>
  </div>
</section>

</body>
</html>
```